Agriculture Business Need a Responsive Web Design

We need a Responsive Web Design for a Agriculture Business
We deliver agriculture data insight for farmers, media, salespersons and other that have an interrest in Agriculture.
Our products is a Velmorix - a application that helps people with insight on farms, and what this farms have deliveried of products. Products like Milk, grains, eggs, slaughtering of livestock, chicken, sheep and other slaughter of animals. Data about size of farms. We deliver stats about these farms. Compeare farms.

Target Market(s)

Agriculture businesses

Industry/Entity Type

Agriculture

Number of Pages Required

1 page

Font styles to use
Sans Serif

Requirements
Must have
• Responsive design. I.e the design shall be used on smartphones to desktop browsers. I think 2 columns on big screens that will collapse to 1 one small screens.

```html
<!DOCTYPE html>
<html lang="en">
<head>
<meta charset="utf-8">
<title>Velmorix — Agriculture Data Insight</title>
<link href="https://fonts.googleapis.com/css2?family=Raleway:wght@500;600;700&family=Open+Sans:wght@400;600&display=swap" rel="stylesheet">
<style>
:root{
  --green:#3f7d12;
  --green-dark:#2f6409;
  --green-deep:#24540a;
  --green-light:#7fb82a;
  --text:#555;
  --text-soft:#777;
  --grey-bg:#f1f1f1;
  --white:#fff;
  --earth-1:#6e4a1e;
  --earth-2:#b07a36;
  --earth-3:#d6a55a;
}
*{margin:0;padding:0;box-sizing:border-box}
html,body{width:720px;height:1200px;overflow:hidden;background:var(--white)}
body{position:relative;font-family:"Open Sans",sans-serif;color:var(--text)}
.abs{position:absolute}

/* header */
.site-header{left:0;top:0;width:720px;height:42px;background:linear-gradient(var(--green-light),var(--green) 60%,var(--green-dark))}
.brand{font-family:"Raleway",sans-serif;font-weight:600;color:var(--white);letter-spacing:.5px}
.site-header .brand{left:90px;top:12px;font-size:16px}
.main-nav{left:293px;top:17px;display:flex;gap:20px;font-family:"Raleway",sans-serif;font-weight:600;font-size:7px;color:var(--white);letter-spacing:.3px}

/* hero */
.hero{left:0;top:42px;width:720px;height:380px;background:linear-gradient(180deg,#8a5d24 0%,var(--earth-2) 25%,var(--earth-3) 45%,#a06a2c 70%,var(--earth-1) 100%)}
.hero-card{left:79px;top:66px;width:215px;height:251px;background:linear-gradient(135deg,#fafafa,#ececec);text-align:center}
.hero-title{position:absolute;left:0;width:100%;top:88px;font-family:"Raleway",sans-serif;font-weight:700;font-size:27px;color:var(--green)}
.hero-text{position:absolute;left:24px;width:167px;top:129px;font-family:"Raleway",sans-serif;font-weight:500;font-size:9.6px;line-height:14.5px;color:#555}
.slider-dots{position:absolute;left:51px;top:206px;display:flex;gap:8px}
.slider-dots span{width:34px;height:1px;background:#ddd}
.slider-dots span.active{height:2px;background:var(--green)}
.hero-photo{left:294px;top:66px;width:347px;height:251px;background:linear-gradient(180deg,#3d6fb0 0%,#8fb4d8 30%,#9a9a3c 48%,#6f7d1e 70%,#3e4a12 100%)}
.welcome{left:0;width:720px;top:333px;text-align:center;color:var(--white)}
.welcome h1{font-family:"Raleway",sans-serif;font-weight:700;font-size:13px;letter-spacing:-.2px}
.welcome p{margin:6px auto 0;width:350px;font-family:"Raleway",sans-serif;font-weight:700;font-size:6.4px;line-height:11.4px;text-transform:uppercase}

/* services */
.services-bg{left:0;top:392px;width:720px;height:272px}
.service{top:472px;width:164px;height:160px;text-align:center}
.service h2{font-family:"Raleway",sans-serif;font-weight:700;font-size:11.5px;color:var(--green);margin-top:8px}
.service svg{display:block;margin:16px auto 0}
.service p{margin:14px auto 0;width:120px;font-size:6.4px;line-height:11.5px;color:var(--text)}
.btn-more{display:inline-block;margin-top:9px;padding:3px 8px;background:var(--white);border:1px solid #e6e6e6;font-size:6.4px;color:var(--text-soft)}
.divider{top:472px;width:1px;height:160px;background:#e2e2e2}

/* products */
.products-head{left:0;width:720px;top:672px;text-align:center}
.products-head h2{font-family:"Raleway",sans-serif;font-weight:700;font-size:12px;color:var(--green)}
.products-head p{margin-top:4px;font-size:6.6px;color:var(--green)}
.tile{border:1px solid #fff}
.tile-label{position:absolute;right:6px;bottom:6px;background:rgba(255,255,255,.88);font-family:"Raleway",sans-serif;font-weight:500;font-size:9.5px;line-height:10px;color:#666;padding:4px 7px;text-align:right}

/* footer */
.contact-band{left:0;top:992px;width:720px;height:56px;background:var(--green-dark)}
.social{left:112px;top:1010px;display:flex;gap:4px}
.social span{width:20px;height:20px;border-radius:50%;background:#3e78c0}
.contact-item{font-family:"Raleway",sans-serif;font-weight:600;font-size:9.5px;color:var(--white);display:flex;align-items:center;gap:9px}
.footer-main{left:0;top:1048px;width:720px;height:130px;background:radial-gradient(ellipse at 45% 100%,#a6cf2c 0%,#6da31c 45%,var(--green) 100%)}
.footer-col h3{font-family:"Raleway",sans-serif;font-weight:600;font-size:9.6px;color:var(--white)}
.quick-links{list-style:none;margin-top:8px}
.quick-links li{font-size:6.6px;line-height:14.4px;color:var(--white)}
.email-field{margin-top:9px;width:120px;height:19px;background:var(--white);font-size:6px;color:#888;padding:6px 8px;display:flex;justify-content:space-between;align-items:center}
.btn-subscribe{margin-top:4px;width:120px;height:20px;background:var(--green-deep);font-family:"Raleway",sans-serif;font-weight:600;font-size:9.5px;color:var(--white);text-align:center;line-height:20px}
.about-text{margin-top:9px;width:115px;font-size:6.4px;line-height:11.6px;color:#eef6dc;text-align:justify}
.footer-main .brand{left:522px;top:1108px;font-size:16px}
.copyright{left:0;top:1178px;width:720px;height:22px;background:var(--green-deep);text-align:center;font-family:Arial,sans-serif;font-size:5.8px;line-height:22px;color:#9fbf7a}
</style>
</head>
<body>

<header class="site-header abs">
  <div class="brand abs">VELMORIX</div>
  <nav class="main-nav abs">
    <span>HOME</span><span>ABOUT US</span><span>SERVICES</span><span>PRODUCTS</span><span>PARTNERS</span><span>CONTACT US</span>
  </nav>
</header>

<section class="hero abs" role="img" aria-label="Harvested golden field with a combine at sunset"></section>
<svg class="services-bg abs" viewBox="0 0 720 272" width="720" height="272" aria-hidden="true">
  <path d="M0 0 Q360 40 720 0 L720 240 Q360 280 0 240 Z" fill="var(--grey-bg)"/>
</svg>

<div class="hero-card abs">
  <div class="hero-title">VELMORIX</div>
  <p class="hero-text">We deliver agriculture data insight for farmers, media and others who have an interest in Agriculture.</p>
  <div class="slider-dots"><span class="active"></span><span></span><span></span></div>
</div>
<div class="hero-photo abs" role="img" aria-label="Close-up of green wheat ears under a blue sky"></div>

<div class="welcome abs">
  <h1>WELCOME TO VELMORIX COMPANY</h1>
  <p>Quisque ad pretium eros sagittis dui eget mauris rhoncus nec habitasse himenaeos parturient elit diam malesuada posuere diam ornare a ultricies ullamcorper ullamcorper in interdum.</p>
</div>

<svg class="abs" style="left:338px;top:402px" width="44" height="22" viewBox="0 0 44 22" aria-label="Slide controls">
  <path d="M0 22 A22 22 0 0 1 44 22 Z" fill="#fff"/>
  <line x1="22" y1="8" x2="22" y2="20" stroke="#ddd" stroke-width="0.8"/>
  <path d="M16 9 L12 14 L16 19" fill="none" stroke="#666" stroke-width="1.2"/>
  <path d="M28 9 L32 14 L28 19" fill="none" stroke="#666" stroke-width="1.2"/>
</svg>

<!-- services -->
<div class="service abs" style="left:115px">
  <h2>AGRICULTURE</h2>
  <svg width="32" height="24" viewBox="0 0 32 24" aria-hidden="true">
    <rect x="6" y="3" width="10" height="9" fill="none" stroke="#555" stroke-width="1.4"/>
    <rect x="4" y="11" width="22" height="5" fill="#f0a830" stroke="#555" stroke-width="1.2"/>
    <circle cx="9" cy="18" r="5" fill="#fff" stroke="#555" stroke-width="1.4"/>
    <circle cx="9" cy="18" r="1.8" fill="#7fb82a"/>
    <circle cx="24" cy="19" r="3.5" fill="#fff" stroke="#555" stroke-width="1.4"/>
    <circle cx="24" cy="19" r="1.3" fill="#7fb82a"/>
  </svg>
  <p>Beciegast nveriti vitaesaert asety kertya aset aplicabrde ertyas nemo eniptaiades.</p>
  <span class="btn-more">Read More</span>
</div>
<div class="divider abs" style="left:278px"></div>
<div class="service abs" style="left:278px">
  <h2>FARMS</h2>
  <svg width="28" height="24" viewBox="0 0 28 24" aria-hidden="true">
    <path d="M3 23 L3 9 L14 2 L25 9 L25 23 Z" fill="#e9a33a" stroke="#555" stroke-width="1.4"/>
    <rect x="8" y="12" width="12" height="11" fill="#fff" stroke="#555" stroke-width="1.2"/>
    <path d="M8 12 L20 23 M20 12 L8 23" stroke="#555" stroke-width="1"/>
  </svg>
  <p>Asety kscabo nerafaes kertyu ersvitae ertyasnemo lasec vasptaiades goertayse.</p>
  <span class="btn-more">Read More</span>
</div>
<div class="divider abs" style="left:442px"></div>
<div class="service abs" style="left:442px">
  <h2>OTHER SERVICE</h2>
  <svg width="32" height="24" viewBox="0 0 32 24" aria-hidden="true">
    <path d="M8 2 L8 23 M4 2 L4 7 Q8 10 12 7 L12 2" fill="none" stroke="#555" stroke-width="1.4"/>
    <path d="M16 8 L28 8 M18 8 L19 4 L25 4 L26 8" fill="#e9a33a" stroke="#555" stroke-width="1.2"/>
    <path d="M15 23 L16 15 L28 15 L29 23 Z" fill="#e9a33a" stroke="#555" stroke-width="1.2"/>
  </svg>
  <p>Miiasrdas nveriti vitaesaert aplicabrdasety kertya asee ertyas nemo eniptaiades</p>
  <span class="btn-more">Read More</span>
</div>

<!-- products -->
<div class="products-head abs">
  <h2>PRODUCTS</h2>
  <p>Lorem ipsum dolor sit amet, consectetuer adipiscing elit. Praesent vestibulum molestie lacus</p>
</div>

<div class="tile abs" style="left:79px;top:717px;width:143px;height:128px;background:linear-gradient(160deg,#dfe4ea,#c9cfd6 60%,#b9a27a)" role="img" aria-label="Glass and bottle of milk on burlap"><span class="tile-label">Milk</span></div>
<div class="tile abs" style="left:222px;top:717px;width:184px;height:128px;background:linear-gradient(180deg,#f6e8b0,#e0b24a 45%,#b97f23)" role="img" aria-label="Golden grain field in sunlight"><span class="tile-label">Grains</span></div>
<div class="tile abs" style="left:406px;top:717px;width:117px;height:128px;background:linear-gradient(160deg,#f3f3f3,#e8a066 45%,#a8743a)" role="img" aria-label="Brown eggs in a straw nest"><span class="tile-label">Eggs</span></div>
<div class="tile abs" style="left:523px;top:717px;width:118px;height:128px;background:linear-gradient(180deg,#4d77b5,#a9c3de 40%,#6c8a36 70%,#4f6a24)" role="img" aria-label="Cattle grazing in a meadow"><span class="tile-label">Slaughtering<br>of livestock</span></div>
<div class="tile abs" style="left:79px;top:845px;width:234px;height:128px;background:linear-gradient(180deg,#6e7a3a,#8a5a2a 45%,#5e7a22)" role="img" aria-label="Hens on green grass"><span class="tile-label">Chicken</span></div>
<div class="tile abs" style="left:313px;top:845px;width:184px;height:128px;background:linear-gradient(180deg,#eef0ec,#cfd2c6 55%,#a9ab98)" role="img" aria-label="Sheep standing in a flock"><span class="tile-label">Sheep</span></div>
<div class="tile abs" style="left:497px;top:845px;width:144px;height:128px;background:linear-gradient(160deg,#3f6a1a,#8a8270 50%,#5a5a4a)" role="img" aria-label="Rabbits on a log in greenery"><span class="tile-label">Other slaughter<br>of animals</span></div>

<!-- footer -->
<section class="contact-band abs"></section>
<div class="social abs" aria-label="Social links"><span></span><span style="background:#4aa3df"></span><span style="background:#d2463a"></span><span style="background:#3a8fc4"></span></div>
<div class="contact-item abs" style="left:256px;top:1013px">
  <svg width="16" height="12" viewBox="0 0 16 12" aria-hidden="true"><rect x=".7" y=".7" width="14.6" height="10.6" fill="none" stroke="#fff" stroke-width="1"/><path d="M1 1 L8 7 L15 1" fill="none" stroke="#fff" stroke-width="1"/></svg>
  <span>Email : info@velmorix-mail.com</span>
</div>
<div class="contact-item abs" style="left:440px;top:1006px">
  <svg width="17" height="16" viewBox="0 0 17 16" aria-hidden="true"><path d="M1 8 L8.5 1.5 L16 8 M3 6.5 L3 15 L14 15 L14 6.5" fill="none" stroke="#fff" stroke-width="1"/><rect x="7" y="10" width="3" height="5" fill="none" stroke="#fff" stroke-width="1"/></svg>
  <span style="line-height:11.5px">14 Fernhollow Rd Ste 210, Marlow Creek<br>IL 60999-1180</span>
</div>

<footer class="footer-main abs"></footer>
<div class="footer-col abs" style="left:107px;top:1063px">
  <h3>Quick Links</h3>
  <ul class="quick-links"><li>Home</li><li>About Us</li><li>Services</li><li>Products</li><li>Partners</li><li>Contact Us</li></ul>
</div>
<div class="footer-col abs" style="left:232px;top:1063px">
  <h3>Newsletter</h3>
  <div class="email-field"><span>Email id</span>
    <svg width="8" height="6" viewBox="0 0 8 6" aria-hidden="true"><rect x=".4" y=".4" width="7.2" height="5.2" fill="none" stroke="#999" stroke-width=".7"/><path d="M.5 .5 L4 3.5 L7.5 .5" fill="none" stroke="#999" stroke-width=".7"/></svg>
  </div>
  <div class="btn-subscribe">Subscribe</div>
</div>
<div class="footer-col abs" style="left:386px;top:1063px">
  <h3>About Us</h3>
  <p class="about-text">Ullamcorper fusce quam nibh in ultrices nec ullamcorper dolor adipiscing gravida semper blandit nostra mi urna natoque.Vulputate vitae fermentum nascetur a pulvinar nulla eget sed purus potenti at.</p>
</div>
<div class="brand abs" style="left:522px;top:1108px;font-size:16px">VELMORIX</div>

<div class="copyright abs">All Rights Reserved. Copyrights @ 2016 company name</div>

</body>
</html>
```